Ridgely Forge business card for handing simple contact information and generating service awareness

Utilizing the attached logo(s), generate a professional, but approachable, card conveying a sense of capability and integrity. Please only use one logo of the four attached; the different colors are all acceptable, but preference will be given to a design integrating a teal/turquoise logo,

I do not know where to put in the contact information or details?

Target Market(s)

Agriculture, Farming, Timber, Forestry, Construction, Crane Service

Industry/Entity Type

Contact Information for Business Card

Name, Phone Number, email address

Colors

Designer to choose colors to be used in the design.

Requirements
Nice to have
• It would be great to have either a mountain or one of the attached cranes as a backdrop on the rear of the card. Simple watermarks and/or Debossing is also great

```html
<!DOCTYPE html>
<html lang="en">
<head>
<meta charset="utf-8">
<title>Ridgely Forge — Business Card</title>
<link rel="stylesheet" href="https://fonts.googleapis.com/css2?family=Archivo:wght@400;600;800&display=swap">
<style>
  :root {
    --backdrop: #3a3a3a;
    --teal: #2a6b61;
    --teal-faint: rgba(42, 107, 97, 0.07);
    --paper: #ffffff;
    --ink: #4a4a4a;
    --ink-soft: #8a8a8a;
    --rule: #d9d9d9;
  }
  * { box-sizing: border-box; margin: 0; padding: 0; }
  html, body { width: 1200px; height: 689px; overflow: hidden; }
  body {
    background: var(--backdrop);
    font-family: "Archivo", Arial, sans-serif;
    position: relative;
  }
  .card {
    position: absolute;
    top: 196px;
    width: 520px;
    height: 297px;
    border-radius: 16px;
    overflow: hidden;
  }
  .card--front { left: 50px; background: var(--teal); }
  .card--back  { left: 630px; background: var(--paper); }

  .front-wordmark {
    position: absolute;
    inset: 0;
    display: flex;
    align-items: center;
    justify-content: center;
    gap: 14px;
  }
  .front-wordmark .mark-dot {
    width: 34px; height: 34px; border-radius: 50%;
    background: var(--paper);
  }
  .front-wordmark .name {
    color: var(--paper);
    font-weight: 800;
    font-size: 40px;
    letter-spacing: 1px;
    text-transform: uppercase;
  }

  .back-backdrop {
    position: absolute;
    left: 40px; top: 70px;
    width: 250px; height: 190px;
    border-radius: 50% 50% 8px 8px;
    background: radial-gradient(ellipse at 50% 40%, rgba(42,107,97,0.09), rgba(42,107,97,0.02) 70%);
  }
  .back-wordmark {
    position: absolute;
    right: 30px; top: 34px;
    display: flex; align-items: center; gap: 8px;
  }
  .back-wordmark .mark-dot {
    width: 18px; height: 18px; border-radius: 50%;
    background: var(--teal);
  }
  .back-wordmark .name {
    color: var(--teal);
    font-weight: 800;
    font-size: 22px;
    text-transform: uppercase;
    letter-spacing: 0.5px;
  }
  .divider {
    position: absolute;
    left: 30px; right: 30px; top: 100px;
    height: 1px; background: var(--rule);
  }
  .address {
    position: absolute;
    right: 30px; top: 114px;
    text-align: right;
    color: var(--ink);
    font-size: 13px;
    line-height: 1.35;
  }
  .person {
    position: absolute;
    left: 30px; top: 180px;
  }
  .person .full-name {
    color: var(--teal);
    font-weight: 600;
    font-size: 22px;
  }
  .person .role {
    color: var(--ink-soft);
    font-size: 12px;
    margin-top: 1px;
  }
  .person .rule {
    width: 200px; height: 1px; background: var(--rule);
    margin: 8px 0 6px;
  }
  .contact-list { list-style: none; }
  .contact-list li {
    display: flex; align-items: center; gap: 8px;
    color: var(--ink);
    font-size: 13px;
    line-height: 1.5;
  }
  .contact-list svg { width: 12px; height: 12px; fill: var(--teal); flex: none; }
</style>
</head>
<body>

<section class="card card--front" aria-label="Card front">
  <div class="front-wordmark">
    <span class="mark-dot"></span>
    <span class="name">Ridgely Forge</span>
  </div>
</section>

<section class="card card--back" aria-label="Card back">
  <div class="back-backdrop" role="img" aria-label="Faint mountain and forest backdrop"></div>

  <div class="back-wordmark">
    <span class="mark-dot"></span>
    <span class="name">Ridgely Forge</span>
  </div>

  <div class="divider"></div>

  <address class="address" style="font-style:normal">
    412 Cedar Bend Road<br>
    Fernhill, Canada 20815<br>
    www.ridgelyforge.com
  </address>

  <div class="person">
    <p class="full-name">Dale Harlow</p>
    <p class="role">President</p>
    <div class="rule"></div>
    <ul class="contact-list">
      <li>
        <svg viewBox="0 0 12 12" aria-hidden="true"><path d="M1 4h10v6H1z M3 2h6v2H3z"/></svg>
        555-210-4417
      </li>
      <li>
        <svg viewBox="0 0 12 12" aria-hidden="true"><path d="M3 0h6a1 1 0 0 1 1 1v10a1 1 0 0 1-1 1H3a1 1 0 0 1-1-1V1a1 1 0 0 1 1-1zm0 1.5v8h6v-8z"/></svg>
        555-382-9061
      </li>
      <li>
        <svg viewBox="0 0 12 12" aria-hidden="true"><path d="M0 2h12v8H0z M0 2l6 4 6-4" stroke="#fff" stroke-width="0.8"/></svg>
        hello@ridgelyforge.com
      </li>
    </ul>
  </div>
</section>

</body>
</html>
```